quillora.link quillora.space quillora.press website

The website is named QUILLORA and it will have 3 domain names. quillora.link, press, space.
I'd like it to be viewed on Pads, pcs and phones.

page menu:

quillora.link(start page): presentation of company. (creative, design, app, new product innovation.)
Here we'll need sosial media icons: twitter, instagram, facebook, linkedin. (light but some 'fruity' colors)

quillora.press: blog. It will be a 75% picture blog > rest will be text. I need to be able to resize pictures and shape columns to picture size. (light but some 'fruity' colors)

quillora.space : the fun part of this web design, however, on entering the page I'd like a non-disclosure agreement where viewer simply click "yes, I agree" after filling out contact info. (check attached document)
We will have space here for uploading PDF files viewers can download. There is also a blog space here to tell in brief about the PDF file. (maybe a space/sci-fi theme her e.g spacechimp, Laika the space dog?)

I will attach the logo here I want you to use > and develop for the .space .press webpage. The logo i uploaded is for the .link page.

Target Market(s)

venture capitalists

Number of Pages Required

3 page

Requirements
Must have
• a few 'fruity colors' but mostly white and grey

```html
<!DOCTYPE html>
<html lang="en">
<head>
<meta charset="utf-8">
<title>Quillora Link</title>
<link href="https://fonts.googleapis.com/css2?family=Arimo:wght@400;700&family=Ubuntu:wght@400&family=Cabin:ital,wght@1,700&display=swap" rel="stylesheet">
<style>
:root{
  --green:#4f9338;
  --green-dark:#2f6f2a;
  --red:#dc4a35;
  --red-title:#d2321f;
  --pink:#f8dcdc;
  --ink:#222;
  --grey:#555;
  --line:#e2e2e2;
  --white:#fff;
}
*{margin:0;padding:0;box-sizing:border-box}
html,body{width:858px;height:1200px;overflow:hidden;background:var(--white)}
body{position:relative;font-family:Arimo,Arial,sans-serif;color:var(--ink)}
.abs{position:absolute}
.topbar{left:235px;top:0;right:0;height:26px;background:var(--pink);clip-path:polygon(30px 0,100% 0,100% 100%,0 100%)}
.contact{top:7px;font-size:11px;color:#555}
.contact.mail{left:483px}
.contact.phone{left:605px;display:flex;align-items:center;gap:4px}
.socials{left:717px;top:5px;display:flex;gap:6px}
.socials span{width:15px;height:15px;background:var(--red)}
.nav{top:26px;left:449px;display:flex;height:30px;font-size:11px;color:#333}
.nav a{display:flex;align-items:center;padding:0 18px;text-decoration:none;color:inherit;border-right:1px solid #ddd;height:12px;margin-top:9px}
.nav a:last-child{border:none}
.nav a.active{background:var(--green);color:#fff;height:30px;margin-top:0;padding:0 19px;border:none}
.navline{top:56px;left:0;right:0;height:1px;background:#ddd}
.hero{top:56px;left:0;width:858px;height:397px;background:linear-gradient(90deg,#1d3f5a,#3f8fb3 45%,#6fb7d2 55%,#234a66)}
.logo-panel{top:0;left:0;width:205px;height:70px;background:#fff;clip-path:polygon(0 0,100% 0,100% 80%,185px 100%,0 100%)}
.logo{left:64px;top:22px;font-weight:700;font-size:22px;color:var(--ink);letter-spacing:1px}
.caption{top:418px;left:0;width:858px;height:35px;background:rgba(20,25,30,.75);color:#fff;font-size:16px;display:flex;align-items:center;justify-content:center}
.arrow{top:223px;width:24px;height:24px;background:#333;border:1px solid #777;display:flex;align-items:center;justify-content:center}
.title{left:0;width:858px;text-align:center;font-family:Ubuntu,sans-serif;font-size:24px;color:var(--green-dark)}
.title em{font-style:normal;color:var(--red-title)}
.rule{left:288px;width:290px;height:1px;background:var(--line)}
.rule::after{content:"";position:absolute;left:120px;top:-1px;width:48px;height:3px;background:var(--green)}
.intro{top:541px;left:68px;width:730px;text-align:center;font-size:11px;line-height:16px;color:var(--ink)}
.intro p+p{margin-top:6px}
.more{top:642px;left:0;width:858px;text-align:center;font-size:10px;font-weight:700;text-decoration:underline}
.band{top:697px;left:0;width:858px;height:123px;background:linear-gradient(90deg,#d8503c,#e06a55 50%,#d8503c)}
.band p{position:absolute;top:30px;left:60px;width:738px;text-align:center;color:#fff;font-family:Cabin,sans-serif;font-style:italic;font-weight:700;font-size:20px;line-height:34px}
.card{top:907px;width:186px;height:195px;text-align:center}
.card.on{background:var(--green);color:#fff;clip-path:polygon(0 0,155px 0,100% 30px,100% 100%,30px 100%,0 165px)}
.badge{margin:14px auto 0;width:84px;height:84px;border-radius:50%;border:3px solid var(--green);padding:4px}
.badge span{display:block;width:100%;height:100%;border-radius:50%;background:var(--green)}
.card.on .badge{border-color:var(--green-dark)}
.card.on .badge span{background:var(--green-dark)}
.card h3{font-weight:400;font-size:14px;margin-top:12px}
.card p{font-size:11px;line-height:16px;margin-top:7px;color:#333;padding:0 10px}
.card.on p{color:#fff}
.foot{top:1158px;left:0;width:858px;height:42px;background:var(--red)}
.foot-tab{top:1135px;left:648px;width:210px;height:25px;background:var(--red);clip-path:polygon(22px 0,100% 0,100% 100%,0 100%)}
.foot-line{top:1133px;left:646px;width:212px;height:26px;background:var(--green);clip-path:polygon(22px 0,100% 0,100% 3px,24px 3px,3px 100%,0 100%)}
.foot-rule{top:1155px;left:0;width:650px;height:3px;background:var(--green)}
.copy{top:1171px;left:63px;font-size:8px;color:#fff}
.foot-logo{top:1150px;left:702px;font-weight:700;font-size:16px;color:var(--ink);letter-spacing:1px}
</style>
</head>
<body>
<div class="abs topbar"></div>
<div class="abs contact mail">sales@brevanto.com</div>
<div class="abs contact phone">
  <svg width="16" height="16" viewBox="0 0 16 16"><circle cx="8" cy="8" r="7" fill="none" stroke="#dc4a35" stroke-width="1.3"/><path d="M6 4.5l1.5 1.7-.8 1.1c.5 1 1.2 1.7 2.2 2.2l1.1-.8 1.7 1.5-1 1.3C7.8 11 5 8.2 4.6 5.5z" fill="#dc4a35"/></svg>
  (555) 014 2290
</div>
<div class="abs socials" aria-label="Social links"><span></span><span></span><span></span><span></span></div>
<nav class="abs nav"><a class="active">Home</a><a>About</a><a>Services</a><a>Our Work</a><a>Contact</a></nav>
<div class="abs navline"></div>

<div class="abs hero" role="img" aria-label="Businessman touching a glowing network of human resources icons"></div>
<div class="abs logo-panel"></div>
<div class="abs logo">QUILLORA</div>
<div class="abs arrow" style="left:4px"><svg width="8" height="10"><path d="M6 1L2 5l4 4" stroke="#fff" stroke-width="2" fill="none"/></svg></div>
<div class="abs arrow" style="left:828px"><svg width="8" height="10"><path d="M2 1l4 4-4 4" stroke="#fff" stroke-width="2" fill="none"/></svg></div>
<div class="abs caption">Lorem Ipsum Dolor Sit Amet Consectetuer Adipiscing Elit Sed Diam Nonummy Nibh</div>

<h1 class="abs title" style="top:485px;font-weight:400">Welcome to <em>Quillora Link</em></h1>
<div class="abs rule" style="top:524px"></div>
<div class="abs intro">
  <p>Lorem ipsum dolor sit amet, consectetuer adipiscing elit, sed diam nonummy nibh euismod tincidunt ut laoreet dolore magna aliquam erat volutpat. Ut wisi enim ad minim veniam, quis nostrud exerci tation ullamcorper suscipit lobortis nisl ut aliquip ex ea commodo consequat. Duis autem vel eum iriure dolor in hendrerit in vulputate velit esse molestie consequat, vel illum dolore eu feugiat nulla facilisis at vero eros et accumsan et iusto odio dignissim qui blandit praesent luptatum zzril delenit augue duis dolore te feugait nulla facilisi.</p>
  <p>We are committed to providing our customers with quality products, designs and 100% Work Satisfaction</p>
</div>
<div class="abs more">Read More</div>

<section class="abs band" role="img" aria-label="Office silhouettes tinted red">
  <p>We Strive To Out Work Our Competition With An Effective Approach And A Powerful Skill Set, Which Is Why Were Industry Leading.</p>
</section>

<h2 class="abs title" style="top:834px;font-weight:400">Our <em>Services</em></h2>
<div class="abs rule" style="top:866px"></div>

<div class="abs card" style="left:52px"><div class="badge" role="img" aria-label="Creative icon"><span></span></div><h3>Creative</h3><p>Lorem ipsum dolor sit amet, consectetuer adipiscing elit, sed diam nonummy nibh.</p></div>
<div class="abs card on" style="left:242px"><div class="badge" role="img" aria-label="App development icon"><span></span></div><h3>App Development</h3><p>Lorem ipsum dolor sit amet, consectetuer adipiscing elit, sed diam nonummy nibh.</p></div>
<div class="abs card" style="left:440px"><div class="badge" role="img" aria-label="New product innovations icon"><span></span></div><h3>New Product Innovations</h3><p>Lorem ipsum dolor sit amet, consectetuer adipiscing elit, sed diam nonummy nibh.</p></div>
<div class="abs card" style="left:630px"><div class="badge" role="img" aria-label="Design icon"><span></span></div><h3>Design</h3><p>Lorem ipsum dolor sit amet, consectetuer adipiscing elit, sed diam nonummy nibh.</p></div>

<div class="abs foot"></div>
<div class="abs foot-tab"></div>
<div class="abs foot-line"></div>
<div class="abs foot-rule"></div>
<div class="abs copy">Copyright© 2016 &nbsp;Quillora Link &nbsp;All rights reserved</div>
<div class="abs foot-logo">QUILLORA</div>
</body>
</html>
```